Brochure Design Project

We sell and install rollout shelves for existing kitchen and bathroom cabinets. These rollout shelves are made of wood with dovetail joints. We also organize cabinets with pullouts, lazy susans, trash can pullouts, drawer organizers, and offer a selection of cabinet handles and knobs that we can also install.

Need extra days to review

```html
<!DOCTYPE html>
<html lang="en">
<head>
<meta charset="utf-8">
<title>Tidy Nook Cabinets – Brochure Outside</title>
<link href="https://fonts.googleapis.com/css2?family=Ubuntu:wght@400;500;700&family=Open+Sans:wght@600;700&family=Montserrat:wght@800&display=swap" rel="stylesheet">
<style>
  :root{
    --green:#6fe32b;
    --green-dark:#4fc41a;
    --ink:#1f1f1f;
    --muted:#4a4a4a;
    --tan:#b8622a;
    --bullet:#e6a46c;
    --paper:#ffffff;
    --paper-soft:#f2f2f2;
    --stage:#3d3d3d;
    --wood:#b27a45;
    --wood-light:#e3c594;
    --cream:#e9e4da;
  }
  *{box-sizing:border-box;margin:0;padding:0}
  html,body{width:1200px;height:974px;overflow:hidden;background:var(--stage)}
  .brochure{position:absolute;left:66px;top:72px;width:1068px;height:830px;background:var(--paper);
    font-family:"Ubuntu",sans-serif;color:var(--ink);box-shadow:0 6px 18px rgba(0,0,0,.4);overflow:hidden}
  .artwork{position:absolute;inset:0}
  .panel-text{position:absolute}
  .showroom{left:28px;top:52px;width:306px;font-size:12.6px;line-height:16px}
  .showroom h2{font-family:"Open Sans",sans-serif;font-weight:700;color:var(--green);font-size:21px;text-align:center;margin-bottom:6px;letter-spacing:.3px}
  .showroom p{text-align:justify}
  .product-list{list-style:none;margin:8px 0 10px 0}
  .product-list li{position:relative;padding-left:17px;line-height:20.8px;font-size:12.6px}
  .product-list li::before{content:"";position:absolute;left:3px;top:9px;width:4px;height:4px;border-radius:50%;background:var(--bullet)}
  .showroom .note{margin-bottom:6px}
  .brand-name{position:absolute;transform:translateX(-50%);font-family:"Ubuntu",sans-serif;font-weight:700;color:var(--tan);
    font-size:22px;white-space:nowrap;display:flex;align-items:center;gap:7px}
  .brand-name .mark{width:12px;height:12px;background:var(--tan)}
  .contact{left:354px;width:351px;top:590px;text-align:center}
  .contact h3{font-family:"Open Sans",sans-serif;font-weight:700;font-size:21px;color:#333;letter-spacing:-.3px}
  .contact h3 span{color:var(--green)}
  .contact .lead{font-size:11px;color:var(--muted);line-height:15px;margin:4px 30px 0}
  .contact-icons{display:flex;justify-content:center;gap:10px;margin-top:10px}
  .contact-icons span{width:35px;height:35px;border-radius:50%;background:var(--green);display:flex;align-items:center;justify-content:center}
  .phone{font-size:19px;font-weight:700;color:var(--green);margin-top:7px}
  .line{font-size:13.6px;color:#333;line-height:18px}
  .follow{font-size:11px;color:var(--muted);margin-top:10px}
  .social{display:flex;justify-content:center;gap:6px;margin-top:5px}
  .social span{width:20px;height:20px;border-radius:50%;background:var(--green)}
  .headline-box{left:766px;top:613px;width:248px;height:117px;border:1.5px solid var(--green-dark);border-top:none}
  .headline-box::before,.headline-box::after{content:"";position:absolute;top:0;height:1.5px;background:var(--green-dark);width:22px}
  .headline-box::before{left:0}.headline-box::after{right:0}
  .headline{left:740px;width:300px;top:602px;text-align:center}
  .headline .kicker{font-size:16px;color:#222}
  .headline h1{font-family:"Montserrat",sans-serif;font-weight:800;color:var(--green);font-size:44px;line-height:36px;margin-top:7px;letter-spacing:.5px}
  .headline .sub{font-size:16px;line-height:20px;color:#222;margin-top:6px;background:var(--paper);display:inline-block;padding:0 6px}
  .web-strip{left:588px;width:480px;top:793px;text-align:center;font-size:13.6px;letter-spacing:2px;color:#1a1a1a;padding-left:120px}
</style>
</head>
<body>
<main class="brochure">
  <svg class="artwork" width="1068" height="830" viewBox="0 0 1068 830" xmlns="http://www.w3.org/2000/svg">
    <defs>
      <linearGradient id="paperGrad" x1="0" y1="0" x2="1" y2="0">
        <stop offset="0" stop-color="#ececec"/><stop offset=".5" stop-color="#fafafa"/><stop offset="1" stop-color="#f0f0f0"/>
      </linearGradient>
      <linearGradient id="kitchenGrad" x1="0" y1="0" x2="1" y2="1">
        <stop offset="0" stop-color="#d9b79a"/><stop offset=".45" stop-color="#a9682f"/><stop offset="1" stop-color="#6e4426"/>
      </linearGradient>
      <linearGradient id="whiteKitchenGrad" x1="0" y1="0" x2="1" y2="1">
        <stop offset="0" stop-color="#d8d2c6"/><stop offset=".6" stop-color="#ece8df"/><stop offset="1" stop-color="#5a544c"/>
      </linearGradient>
      <linearGradient id="drawerGrad" x1="0" y1="0" x2="0" y2="1">
        <stop offset="0" stop-color="#f1e2c4"/><stop offset=".6" stop-color="#d9b98a"/><stop offset="1" stop-color="#6b5a4a"/>
      </linearGradient>
      <linearGradient id="ringGrad" x1="0" y1="0" x2="1" y2="1">
        <stop offset="0" stop-color="#ffffff"/><stop offset="1" stop-color="#cfcfcf"/>
      </linearGradient>
    </defs>

    <!-- middle and right panel paper -->
    <rect x="354" y="0" width="714" height="830" fill="url(#paperGrad)"/>
    <line x1="354" y1="0" x2="354" y2="830" stroke="#e0e0e0"/>
    <line x1="705" y1="0" x2="705" y2="830" stroke="#e6e6e6"/>

    <!-- left panel top swoosh -->
    <path d="M0 0 H276 C200 22 110 36 0 46 Z" fill="var(--green)"/>
    <path d="M0 50 C110 40 200 24 276 0" fill="none" stroke="#d6d6d6" stroke-width="2"/>

    <!-- left panel lower kitchen image -->
    <g role="img" aria-label="Photo of a white kitchen with cabinets and dishwasher">
      <path d="M0 620 C110 585 240 560 354 548 V830 H0 Z" fill="url(#whiteKitchenGrad)"/>
    </g>
    <path d="M0 608 C110 572 240 548 354 538 V548 C240 560 110 585 0 620 Z" fill="var(--green)"/>
    <path d="M0 598 C110 562 240 538 354 528" fill="none" stroke="#e2e2e2" stroke-width="2"/>

    <!-- left circle drawer image -->
    <circle cx="180" cy="558" r="110" fill="url(#ringGrad)"/>
    <g role="img" aria-label="Photo of a wooden rollout drawer on soft close slides">
      <circle cx="180" cy="558" r="98" fill="url(#drawerGrad)"/>
    </g>

    <!-- main kitchen image spanning middle and right panels -->
    <g role="img" aria-label="Photo of a warm wood kitchen with stainless appliances and glass front cabinets">
      <path d="M354 0 H1068 V340 C960 430 840 480 700 470 C600 462 560 420 520 395 C460 380 400 390 354 370 Z" fill="url(#kitchenGrad)"/>
    </g>
    <path d="M354 370 C380 370 410 360 440 352 L440 362 C410 372 380 382 354 386 Z" fill="var(--green)"/>
    <path d="M354 392 C380 390 410 380 440 372" fill="none" stroke="#dcdcdc" stroke-width="1.5"/>
    <path d="M700 470 C840 480 960 430 1068 340 V380 C960 470 840 510 720 500 C705 490 700 480 700 470 Z" fill="var(--green)"/>
    <path d="M690 478 C710 505 840 530 1068 398" fill="none" stroke="#d9d9d9" stroke-width="1.5"/>

    <!-- middle circle drawer image -->
    <circle cx="536" cy="373" r="120" fill="url(#ringGrad)"/>
    <g role="img" aria-label="Photo of two wooden rollout shelves inside a base cabinet">
      <circle cx="536" cy="373" r="107" fill="url(#drawerGrad)"/>
    </g>

    <!-- right panel bottom green band -->
    <path d="M588 830 C720 800 880 772 1068 764 V830 Z" fill="var(--green)"/>
    <path d="M560 830 C700 790 880 762 1068 756" fill="none" stroke="#d9d9d9" stroke-width="1.5"/>
  </svg>

  <section class="panel-text showroom">
    <h2>SHOWROOM</h2>
    <p>Tidy Nook provides a different type of buying experience. We come to our clients home or place of business with our Mobile Showroom and are able to show them all these organizing products:</p>
    <ul class="product-list">
      <li>Rollouts for your pantry and lower cabinets</li>
      <li>Pullouts for your upper cabinets</li>
      <li>New drawers using the original facings</li>
      <li>Add full extension soft close slides</li>
      <li>Lazy Susans</li>
      <li>Blind Corner Units</li>
      <li>Trash Can Pullouts</li>
      <li>Appliance Lifts</li>
      <li>And of course, Cabinet Handles and Knobs!</li>
    </ul>
    <p class="note">(over 1000 samples on the walls of our Mobile Showroom)</p>
    <p>With over 10 years in the business, we can save you time and money. You don’t have to buy new cabinets to get more space. We are able to create more space with the cabinets you already have.</p>
  </section>

  <div class="brand-name" style="left:534px;top:532px"><span class="mark"></span>Tidy Nook Cabinets</div>

  <section class="panel-text contact">
    <h3>GET <span>IN TOUCH</span></h3>
    <p class="lead">To schedule your In-Home estimate please contact us either by phone or email.</p>
    <div class="contact-icons">
      <span><svg width="14" height="20" viewBox="0 0 14 20"><rect x="1" y="1" width="12" height="18" rx="2" fill="none" stroke="#fff" stroke-width="1.6"/><circle cx="7" cy="16" r="1.2" fill="#fff"/></svg></span>
      <span><svg width="20" height="14" viewBox="0 0 20 14"><rect x="1" y="1" width="18" height="12" fill="none" stroke="#fff" stroke-width="1.5"/><path d="M1 1 L10 8 L19 1" fill="none" stroke="#fff" stroke-width="1.5"/></svg></span>
      <span><svg width="20" height="20" viewBox="0 0 20 20" fill="none" stroke="#fff" stroke-width="1.4"><circle cx="10" cy="10" r="8.5"/><ellipse cx="10" cy="10" rx="4" ry="8.5"/><line x1="1.5" y1="10" x2="18.5" y2="10"/><line x1="3" y1="5.5" x2="17" y2="5.5"/><line x1="3" y1="14.5" x2="17" y2="14.5"/></svg></span>
    </div>
    <p class="phone">(555) 014-2290</p>
    <p class="line">hello@tidynookcabinets.com</p>
    <p class="line">www.tidynookcabinets.com</p>
    <p class="follow">Follow Us :</p>
    <div class="social"><span></span><span></span><span></span><span></span></div>
  </section>

  <div class="brand-name" style="left:890px;top:540px"><span class="mark"></span>Tidy Nook Cabinets</div>

  <div class="panel-text headline-box"></div>
  <section class="panel-text headline">
    <p class="kicker">We sell and install</p>
    <h1>ROLLOUT<br>SHELVES</h1>
    <p class="sub">For Existing Kitchen And<br>Bathroom Cabinets</p>
  </section>

  <p class="panel-text web-strip">www.tidynookcabinets.com</p>
</main>
</body>
</html>
```